Full book cover design for FEEDBACK book

The book title is: Feedback
Subtitle: Seek it, give it, connect with it.
Authors: Carl Brenner & Marian Quist
We are looking for a complete book cover design using a combination of my brand colours and that of my co-author (Carl). The colours we use include:

Marian: Blue #1E84AB & Carl: Blue #01275B and white.

An idea on the wording for the back cover is here (open to tweak/shorten it if better that way):

The most dynamic leaders today are focused on increasing effectiveness and improving team cohesion. This book demonstrates how creating a culture of feedback enables both of these things.

Feedback allows for the strengthening of communication and allows individuals to continually learn and grow, with the support of their colleagues.

Marian and Carl have created a unique approach to change the often-negative perception associated with feedback. They created it for you…to unlock the opportunity, freedom and success you can achieve when feedback is implemented and used regularly.

If you are a leader looking for ways to build skills in your people, contribute to their growth and development, and maintain a strong, supportive culture, all while delivering business outcomes, then this is the book for you.

“If you are keen to transform feedback from average to awesome and from being a chore to an art, this book is a must read.”
Victor Lunsky, Bravelane Axton

“In today’s hybrid work environment, greater transparency and empowerment, through developing a feedback culture, is essential.”
Odette Varley, Pelvro

We will also need to allow space for a barcode and the publishers logo (just above it) on the back bottom right hand side.

Target Market(s)

Business leaders

Industry/Entity Type

Business

Font styles to use
Serif
Other font styles liked:
• Open to any other fonts that will suit the design

Colors
0054AA
0677BA
7BADD7
CADEEF
E8F1F8

Requirements
Must have
• Colours: Blue #1E84AB & Blue #01275B and white.
Nice to have
• Something creative and smart but not too busy.

```html
<!DOCTYPE html>
<html lang="en">
<head>
<meta charset="utf-8">
<title>Feedback – Full Book Cover</title>
<link rel="stylesheet" href="https://fonts.googleapis.com/css2?family=Bebas+Neue&family=Fira+Sans:ital,wght@0,400;1,400&family=Montserrat:wght@700&display=swap">
<style>
  :root {
    --navy: #01275B;
    --brand-blue: #1E84AB;
    --spine-blue: #0E4A7E;
    --white: #FFFFFF;
    --quote-yellow: #F4EC6A;
    --photo-light: #E4EBF2;
    --photo-mid: #9FB3C8;
    --photo-dark: #5C7894;
  }
  html, body {
    margin: 0;
    padding: 0;
    width: 1200px;
    height: 844px;
    overflow: hidden;
    background: var(--white);
  }
  .cover {
    position: relative;
    width: 1200px;
    height: 844px;
  }
  .cover-art {
    position: absolute;
    inset: 0;
    display: block;
  }
  .display-type {
    font-family: "Bebas Neue", "Oswald", sans-serif;
    fill: var(--white);
  }
  .author-line {
    font-family: "Montserrat", sans-serif;
    font-weight: 700;
  }
  .author-line .author-primary { fill: var(--navy); }
  .author-line .author-secondary { fill: var(--brand-blue); }
  .author-line .amp { fill: var(--navy); font-size: 22px; }
  .back-copy {
    position: absolute;
    left: 55px;
    top: 202px;
    width: 460px;
    font-family: "Fira Sans", sans-serif;
    font-size: 13.8px;
    line-height: 17.3px;
    color: var(--white);
  }
  .back-copy p {
    margin: 0 0 17px 0;
  }
  .back-copy .endorsement {
    margin-bottom: 17px;
  }
  .back-copy .endorsement p {
    margin: 0;
  }
  .back-copy .endorser {
    font-style: italic;
    color: var(--quote-yellow);
  }
</style>
</head>
<body>
<main class="cover">
  <svg class="cover-art" width="1200" height="844" viewBox="0 0 1200 844" xmlns="http://www.w3.org/2000/svg">
    <!-- Back cover -->
    <rect class="back-panel" x="0" y="0" width="561" height="844" fill="var(--navy)"/>
    <polygon class="back-title-banner" points="107,33 426,33 454,139 107,139" fill="var(--brand-blue)"/>
    <text class="display-type" x="139" y="119" font-size="93" textLength="268" lengthAdjust="spacingAndGlyphs">FEEDBACK</text>
    <rect class="back-rule" x="59" y="170" width="443" height="3.5" fill="var(--white)"/>
    <rect class="barcode-space" x="352" y="707" width="186" height="113" fill="var(--white)"/>

    <!-- Spine -->
    <rect class="spine-edge" x="561" y="0" width="7" height="844" fill="var(--brand-blue)"/>
    <rect class="spine" x="568" y="0" width="60" height="844" fill="var(--spine-blue)"/>
    <g class="spine-type display-type">
      <text transform="translate(580,60) rotate(90)" font-size="50" textLength="138" lengthAdjust="spacingAndGlyphs">FEEDBACK</text>
      <text transform="translate(580,401) rotate(90)" font-size="50" textLength="388" lengthAdjust="spacingAndGlyphs">CARL BRENNER &amp; MARIAN QUIST</text>
    </g>

    <!-- Front cover -->
    <rect class="front-edge" x="628" y="0" width="8" height="844" fill="var(--brand-blue)"/>
    <rect class="front-panel" x="636" y="0" width="564" height="844" fill="var(--white)"/>
    <polygon class="front-title-banner" points="636,24 1140,24 1188,192 636,192" fill="var(--brand-blue)"/>
    <text class="display-type" x="657" y="168" font-size="158" textLength="452" lengthAdjust="spacingAndGlyphs">FEEDBACK</text>

    <defs>
      <linearGradient id="teamPhotoTone" x1="0" y1="0" x2="0" y2="1">
        <stop offset="0" stop-color="var(--photo-light)"/>
        <stop offset="0.55" stop-color="var(--photo-mid)"/>
        <stop offset="1" stop-color="var(--photo-dark)"/>
      </linearGradient>
    </defs>
    <rect class="team-photo" x="636" y="384" width="564" height="342" fill="url(#teamPhotoTone)" role="img" aria-label="Photo of a diverse team meeting around a conference table with a whiteboard of charts"/>

    <polygon class="subtitle-panel" points="853,217 1122,217 1188,390 853,390" fill="var(--navy)"/>
    <g class="subtitle display-type" font-size="56">
      <text x="892" y="267" textLength="113" lengthAdjust="spacingAndGlyphs">SEEK IT,</text>
      <text x="899" y="316" textLength="110" lengthAdjust="spacingAndGlyphs">GIVE IT,</text>
      <text x="892" y="366" textLength="247" lengthAdjust="spacingAndGlyphs">CONNECT WITH IT</text>
    </g>

    <rect class="author-band-top" x="636" y="726" width="564" height="18" fill="var(--brand-blue)"/>
    <rect class="author-band" x="636" y="744" width="564" height="81" fill="var(--white)"/>
    <rect class="author-band-bottom" x="636" y="825" width="564" height="19" fill="var(--brand-blue)"/>
    <text class="author-line" x="695" y="798" font-size="31">
      <tspan class="author-primary">Carl Brenner</tspan><tspan class="amp" dx="6">&amp;</tspan><tspan class="author-secondary" dx="6">Marian Quist</tspan>
    </text>
  </svg>

  <section class="back-copy">
    <p>The most dynamic leaders today are focused on increasing effectiveness and improving team cohesion. This book demonstrates how creating a culture of feedback enables both of these things.</p>
    <p>Feedback allows for the strengthening of communication and allows individuals to continually learn and grow, with the support of their colleagues.</p>
    <p>Marian and Carl have created a unique approach to change the often-negative perception associated with feedback. They created it for you…to unlock the opportunity, freedom and success you can achieve when feedback is implemented and used regularly.</p>
    <p>If you are a leader looking for ways to build skills in your people, contribute to their growth and development, and maintain a strong, supportive culture, all while delivering business outcomes, then this is the book for you.</p>
    <div class="endorsement">
      <p>“If you are keen to transform feedback from average to awesome and from being a chore to an art, this book is a must read.”</p>
      <p class="endorser">Victor Lunsky, Bravelane Axton</p>
    </div>
    <div class="endorsement">
      <p>“In today’s hybrid work environment, greater transparency and empowerment, through developing a feedback culture,<br>&nbsp;is essential.”</p>
      <p class="endorser">Odette Varley, Pelvro</p>
    </div>
  </section>
</main>
</body>
</html>
```